Grand Opening Celebration of Radiant Glow Atelier

We need a flyer designer for a new eyelash and skincare studio that just opened in Aliso Viejo, CA. We specialize in Eyelash enhancement artistry, and perform various services such as vegan/organic spray tans, full body waxing, makeup artistry and customized facials. We are having a Grand opening celebration to make the community aware that we are here, to drum up business and to have locals attend the opening. So I need a flyer that will give the info for that and be appealing to both men and women, as I start to figure out the vendors that will be there I will send their info. SO I would like to just see a couple rough drafts to see if you can do the style I am looking for. My inspirations are vellora, mirel, tox, dean harlow, companies like that. My website is this www.radiantglowatelier.com

Event will be on December 6 at 3:00. 48 Corbel Lane, Aliso Viejo, CA 92601

```html
<!DOCTYPE html>
<html lang="en">
<head>
<meta charset="utf-8">
<title>Radiant Glow Atelier — Grand Opening</title>
<link rel="stylesheet" href="https://fonts.googleapis.com/css2?family=Oswald:wght@400;500;700&family=Open+Sans:wght@400;600&display=swap">
<style>
  :root {
    --ink: #0d0d0d;
    --coral: #f2716e;
    --coral-deep: #e45c5a;
    --white: #ffffff;
    --sun: #f3e21a;
    --photo-warm: #a77c66;
    --photo-dark: #3a2c28;
    --photo-light: #d9c3b6;
  }
  * { margin: 0; padding: 0; box-sizing: border-box; }
  html, body { width: 900px; height: 1200px; overflow: hidden; background: var(--ink); }
  .flyer {
    position: relative; width: 900px; height: 1200px; overflow: hidden;
    background: var(--ink); color: var(--white);
    font-family: "Open Sans", sans-serif;
  }
  .backdrop { position: absolute; inset: 0; }
  .brand {
    position: absolute; left: 56px; top: 54px;
    display: flex; align-items: center; gap: 16px;
  }
  .brand-dot { width: 22px; height: 22px; border-radius: 50%; background: var(--white); }
  .brand-name {
    font-family: "Oswald", sans-serif; font-weight: 500; font-size: 34px;
    letter-spacing: 3px; line-height: 1.05; color: var(--white); text-transform: uppercase;
  }
  .portrait {
    position: absolute; border-radius: 50%; border: 6px solid var(--white);
  }
  .portrait-hat { left: 40px; top: 168px; width: 230px; height: 230px;
    background: radial-gradient(circle at 55% 55%, var(--photo-light), var(--photo-dark) 75%); }
  .portrait-mono { left: 250px; top: 360px; width: 190px; height: 190px;
    background: radial-gradient(circle at 50% 45%, #e2e2e2, #4a4a4a 80%); }
  .portrait-brick { left: 600px; top: 540px; width: 230px; height: 230px;
    background: radial-gradient(circle at 50% 50%, var(--photo-warm), #5a3226 80%); }
  .about { position: absolute; left: 56px; top: 560px; width: 470px; }
  .section-title {
    font-family: "Oswald", sans-serif; font-weight: 500; font-size: 40px;
    color: var(--coral); text-transform: uppercase; letter-spacing: 1px; line-height: 1.1;
  }
  .about p { margin-top: 10px; font-size: 15.5px; line-height: 1.45; color: var(--white); }
  .services { position: absolute; left: 56px; top: 836px; width: 340px; }
  .services ul { list-style: none; margin-top: 14px; }
  .services li {
    position: relative; padding-left: 30px; margin-bottom: 12px;
    font-family: "Oswald", sans-serif; font-size: 22px; line-height: 1.2;
    text-transform: uppercase; letter-spacing: .5px;
  }
  .services li::before {
    content: ""; position: absolute; left: 4px; top: 9px;
    width: 11px; height: 11px; border-radius: 50%; background: var(--coral);
  }
  .headline {
    position: absolute; left: 575px; top: 812px; width: 300px;
    font-family: "Oswald", sans-serif; font-weight: 700; text-transform: uppercase;
  }
  .headline h1 { font-size: 84px; line-height: .95; color: var(--white); }
  .headline .when { margin-top: 16px; font-size: 40px; font-weight: 500; line-height: 1.12; color: var(--ink); }
  .badge { position: absolute; left: 400px; top: 880px; width: 168px; height: 168px; }
  .badge-text {
    position: absolute; inset: 0; display: flex; flex-direction: column;
    align-items: center; justify-content: center;
    font-family: "Oswald", sans-serif; font-weight: 700; font-size: 19px;
    line-height: 1.1; color: var(--ink); text-transform: uppercase; text-align: center;
  }
  .website {
    position: absolute; left: 40px; top: 1118px; padding: 8px 30px;
    background: var(--coral); border-radius: 24px;
    font-size: 19px; font-weight: 600; color: var(--white);
  }
  .social { position: absolute; right: 40px; top: 1116px; display: flex; gap: 10px; }
  .social span { width: 40px; height: 40px; border-radius: 6px; background: var(--white); }
</style>
</head>
<body>
<main class="flyer">
  <svg class="backdrop" width="900" height="1200" viewBox="0 0 900 1200">
    <defs>
      <linearGradient id="heroTone" x1="0" y1="0" x2="1" y2="1">
        <stop offset="0" stop-color="#5b4a44"/>
        <stop offset=".5" stop-color="#b48c76"/>
        <stop offset="1" stop-color="#e6d4c8"/>
      </linearGradient>
    </defs>
    <path d="M390 0 H900 V560 C760 560 620 520 520 440 C450 380 410 300 380 200 Z"
          fill="url(#heroTone)" role="img" aria-label="Photo of a model with long wavy hair"/>
    <path class="wave-top" d="M0 250 C140 230 250 300 330 400 C420 510 560 590 760 560 L900 540 V600
             C740 640 560 640 440 560 C330 480 230 330 0 330 Z" fill="var(--coral)"/>
    <path class="wave-bottom" d="M900 700 C760 720 620 760 520 820 C470 860 440 920 440 1000
             C440 1060 470 1090 520 1100 H900 Z" fill="var(--coral)"/>
    <rect x="0" y="1100" width="900" height="100" fill="var(--ink)"/>
  </svg>

  <header class="brand">
    <span class="brand-dot"></span>
    <span class="brand-name">Radiant Glow<br>Atelier</span>
  </header>

  <div class="portrait portrait-hat" role="img" aria-label="Portrait of a model wearing a black hat"></div>
  <div class="portrait portrait-mono" role="img" aria-label="Black and white portrait of a model"></div>
  <div class="portrait portrait-brick" role="img" aria-label="Portrait of a smiling model by a brick wall"></div>

  <section class="about">
    <h2 class="section-title">About Us</h2>
    <p>At Radiant Glow Atelier our main goal is to benefit our clients both internally and externally. We offer the highest quality alkaline water and antioxidant super foods which act as a perfect pair for feeding your body what it needs. In addition, our wide variety of enhancement services will make you feel your best and are sure to have you leaving with lasting results.</p>
  </section>

  <section class="services">
    <h2 class="section-title">Our Services</h2>
    <ul>
      <li>Eyelash Enhancement Artistry</li>
      <li>Vegan/Organic Spray Tans</li>
      <li>Full Body Waxing</li>
      <li>Makeup Artistry</li>
      <li>Facials</li>
    </ul>
  </section>

  <div class="badge">
    <svg width="168" height="168" viewBox="0 0 168 168">
      <polygon fill="var(--sun)" points="84,2 95,22 114,8 117,31 140,24 134,46 158,48 144,66 164,78 146,92 160,111 137,115 142,138 120,132 114,155 97,142 84,164 71,142 54,155 48,132 26,138 31,115 8,111 22,92 4,78 24,66 10,48 34,46 28,24 51,31 54,8 73,22"/>
    </svg>
    <div class="badge-text"><span>Special</span><span>Activities</span><span>Food</span><span>Music</span></div>
  </div>

  <section class="headline">
    <h1>Grand<br>Opening</h1>
    <p class="when">December 6<br>At 3:00</p>
  </section>

  <footer>
    <p class="website">www.radiantglowatelier.com</p>
    <div class="social" aria-label="Social links"><span></span><span></span><span></span><span></span></div>
  </footer>
</main>
</body>
</html>
```